Brantley Water Taxi and Transport

Need to redesign our business cards to relay that we do freight logistics and water taxi service. We also work with gov. agencies doing environmental clean up, oil spill response, remote site construction and work with many of the air taxi and helicopter services on Kodiak Island. Out website is www.brantleywatertaxi-example.com to get a better idea of what we do.

Contact Information for Business Card

I have a previous business card but it just has the logo on the front, and a sunset picture on the back with the contact info. It does not relay what we do and what we can help with. I like a simple straight forward design over a busy one.

Colors
3176b5
0455a3
cfdfed

Requirements
Must have
• logo, email, website, phone number

```html
<!DOCTYPE html>
<html lang="en">
<head>
<meta charset="utf-8">
<title>Brantley Water Taxi and Transport – Business Card</title>
<link href="https://fonts.googleapis.com/css2?family=Open+Sans:wght@400;600;700&display=swap" rel="stylesheet">
<style>
  :root {
    --navy: #0455a3;
    --deep-navy: #1d4893;
    --sky: #3176b5;
    --ice: #cfdfed;
    --bright-sky: #3fa9e0;
    --white: #ffffff;
    --stage: #e6e9ee;
    --ink: #1e3f7a;
  }
  * { margin: 0; padding: 0; box-sizing: border-box; }
  html, body { width: 1200px; height: 780px; overflow: hidden; }
  body {
    background: var(--stage);
    font-family: "Open Sans", Arial, sans-serif;
    display: flex;
    align-items: center;
    justify-content: center;
    gap: 50px;
  }
  .card {
    width: 525px;
    height: 300px;
    box-shadow: 0 10px 28px rgba(20, 40, 80, 0.18);
    background: var(--white);
    overflow: hidden;
  }
  .card svg { display: block; width: 525px; height: 300px; }
  .person-name { font-size: 27px; font-weight: 400; fill: var(--white); }
  .person-title { font-size: 10px; fill: var(--white); opacity: 0.85; }
  .contact-line { font-size: 13px; fill: var(--white); }
  .company-name { font-weight: 700; fill: var(--navy); }
  .web-address { font-size: 14px; font-weight: 600; fill: var(--white); }
</style>
</head>
<body>

  <!-- Front: contact side -->
  <div class="card card-front">
    <svg viewBox="0 0 525 300" xmlns="http://www.w3.org/2000/svg">
      <defs>
        <linearGradient id="sceneTone" x1="0" y1="0" x2="0" y2="1">
          <stop offset="0" stop-color="#f6a623"/>
          <stop offset="0.35" stop-color="#8fd0f0"/>
          <stop offset="1" stop-color="#3fa9e0"/>
        </linearGradient>
      </defs>
      <rect class="card-base" width="525" height="300" fill="var(--deep-navy)"/>
      <ellipse class="accent-swoosh" cx="455" cy="80" rx="250" ry="205" fill="var(--bright-sky)"/>
      <ellipse class="logo-field" cx="478" cy="72" rx="240" ry="200" fill="var(--white)"/>

      <rect class="logo-illustration" x="375" y="18" width="120" height="80" rx="6"
            fill="url(#sceneTone)" role="img"
            aria-label="Illustration of a transport vessel on the water with ice mountains and a rising sun"/>
      <text class="company-name" x="435" y="126" font-size="20" text-anchor="middle">Brantley</text>
      <text class="company-name" x="435" y="146" font-size="11" text-anchor="middle" font-size-adjust="none">Water Taxi and Transport</text>

      <text class="person-name" x="38" y="128">Your Name</text>
      <text class="person-title" x="90" y="145">Title Gose Here</text>

      <g class="contact-list">
        <g class="contact-phone">
          <path d="M40 178 q-2 6 4 12 q6 6 10 4 l-2 -4 -3 1 q-4 -2 -6 -6 l1 -3 z" fill="var(--white)"/>
          <text class="contact-line" x="62" y="190">123 - 456 - 7890</text>
        </g>
        <g class="contact-mobile">
          <rect x="42" y="198" width="8" height="12" rx="1.5" fill="var(--white)"/>
          <text class="contact-line" x="62" y="210">010 - 000 - 0000</text>
        </g>
        <g class="contact-email">
          <rect x="40" y="219" width="12" height="9" fill="var(--white)"/>
          <path d="M40 219 l6 5 6 -5" fill="none" stroke="var(--deep-navy)" stroke-width="1.2"/>
          <text class="contact-line" x="62" y="230">your@email.com</text>
        </g>
        <g class="contact-address">
          <path d="M46 238 a5 5 0 0 1 5 5 c0 4 -5 9 -5 9 s-5 -5 -5 -9 a5 5 0 0 1 5 -5 z" fill="var(--white)"/>
          <circle cx="46" cy="243" r="1.8" fill="var(--deep-navy)"/>
          <text class="contact-line" x="62" y="250">your address gose here</text>
        </g>
      </g>
    </svg>
  </div>

  <!-- Back: brand side -->
  <div class="card card-back">
    <svg viewBox="0 0 525 300" xmlns="http://www.w3.org/2000/svg">
      <defs>
        <linearGradient id="sceneToneBack" x1="0" y1="0" x2="0" y2="1">
          <stop offset="0" stop-color="#f6a623"/>
          <stop offset="0.35" stop-color="#8fd0f0"/>
          <stop offset="1" stop-color="#3fa9e0"/>
        </linearGradient>
      </defs>
      <rect class="card-base" width="525" height="300" fill="var(--white)"/>
      <rect class="logo-illustration" x="185" y="30" width="155" height="115" rx="8"
            fill="url(#sceneToneBack)" role="img"
            aria-label="Illustration of a transport vessel on the water with ice mountains and a rising sun"/>
      <text class="company-name" x="262" y="190" font-size="40" text-anchor="middle">Brantley</text>
      <text class="company-name" x="262" y="218" font-size="17" text-anchor="middle">Water Taxi and Transport</text>

      <path class="web-band" d="M225 254 H525 V300 H215 Z" fill="var(--deep-navy)"/>
      <text class="web-address" x="505" y="283" text-anchor="end">www.brantleywatertaxi-example.com</text>
    </svg>
  </div>

</body>
</html>
```